Tavosk Engineering Report Template

A word doc report Template for an Engineering Company - Tavosk

Target Market(s)

Construction/Development Industry

Industry/Entity Type

Engineering Consultant

Font styles to use
Sans Serif
Other font styles liked:
• Calibri

Colors
0455a3

Requirements
Must have
• An awesome front page, using the Tavosk Logo (not sure which version yet)
• A great back page
• Good formatting within, different heading styles which look awesome
• Format generally as the the PLW example report, no need to vary
Nice to have
• smart features? easily manipulated? not sure how tricky or smart Word is in this area.
Should not have
• LOCKED features (if possible)

```html
<!DOCTYPE html>
<html lang="en">
<head>
<meta charset="utf-8">
<title>Tavosk Engineering Report Template</title>
<link href="https://fonts.googleapis.com/css2?family=Carlito:wght@400;700&display=swap" rel="stylesheet">
<style>
  :root{
    --brand:#0455a3;
    --brand-mid:#3f86c9;
    --brand-light:#a9c8e8;
    --brand-pale:#dce9f6;
    --ink:#1d1d1d;
    --text:#5a5a5a;
    --rule:#c9c9c9;
    --canvas:#ffffff;
    --dark:#1b1b1b;
  }
  *{margin:0;padding:0;box-sizing:border-box}
  html,body{width:672px;height:1200px;overflow:hidden;background:var(--canvas)}
  body{position:relative;font-family:"Carlito",sans-serif;color:var(--ink)}
  .page{position:absolute;width:196px;height:272px;background:#fff;box-shadow:0 1px 4px rgba(0,0,0,.28)}
  .brand{position:absolute;top:7px;left:0;right:0;display:flex;justify-content:center;align-items:center;gap:3px}
  .brand-square{width:6px;height:6px;background:var(--brand)}
  .brand-name{font-size:5px;font-weight:700;color:var(--brand);letter-spacing:.2px}
  .band{position:absolute;top:20px;left:0;right:0;height:6px}
  .band::before{content:"";position:absolute;left:0;right:0;top:0;height:1px;background:var(--brand-light)}
  .band::after{content:"";position:absolute;left:0;right:0;top:2px;height:3px;background:var(--brand)}
  .footer{position:absolute;bottom:12px;left:16px;right:16px;border-top:.6px solid var(--brand-light);text-align:center;font-size:3.6px;color:var(--text);padding-top:3px}
  .body{position:absolute;top:36px;left:17px;right:17px}
  .h1{font-size:11px;font-weight:700;color:var(--brand);margin-bottom:6px}
  .h2{font-size:5px;font-weight:700;color:var(--ink);margin:4px 0 2px}
  .h3{font-size:4.2px;font-weight:700;color:var(--brand);margin:3px 0 2px}
  .p{font-size:3.3px;line-height:4.4px;color:var(--text);margin-bottom:3px}
  .list{font-size:3.3px;line-height:4.4px;color:var(--text);margin:0 0 3px 6px}
  .list li{margin-bottom:1px}
  .list .sub{margin-left:8px;list-style:circle}
  /* cover */
  .cover-photo{position:absolute;top:28px;left:0;right:0;height:122px;background:radial-gradient(circle at 55% 45%,#b9bcbf 0,#7b7f83 40%,#3d4043 100%)}
  .cover-title{position:absolute;top:160px;left:17px;font-size:12px;font-weight:700;color:var(--ink)}
  .cover-sub{position:absolute;top:175px;left:17px;font-size:5px;color:var(--brand)}
  .cover-meta{position:absolute;top:188px;left:17px;font-size:3.3px;line-height:4.6px;color:var(--text)}
  /* contents */
  .toc{list-style:none;font-size:3.6px;color:var(--text)}
  .toc li{display:flex;align-items:baseline;margin-bottom:6px}
  .toc li span.dots{flex:1;border-bottom:.5px dotted var(--rule);margin:0 2px}
  /* tables */
  .tbl-label{font-size:3.4px;color:var(--text);margin:6px 0 2px}
  table{width:100%;border-collapse:collapse;font-size:3px;color:var(--text)}
  th,td{padding:1.4px 2px;text-align:left;border-bottom:.5px solid var(--rule)}
  th{font-weight:700;color:var(--ink)}
  .tbl-blue th{background:var(--brand);color:#fff}
  .tbl-blue tr:nth-child(even) td{background:var(--brand-pale)}
  .tbl-rule th{border-bottom:1px solid var(--brand)}
  .tbl-dark th{background:var(--dark);color:#fff}
  .tbl-dark tr:nth-child(even) td{background:#efefef}
  td.num,th.num{text-align:right}
  /* charts */
  .charts{display:grid;grid-template-columns:1fr 1fr;gap:10px 8px}
  .chart-title{font-size:3.2px;color:var(--ink);margin-bottom:2px}
  .chart svg{display:block;width:100%;height:auto}
  .disclaimer .p{text-align:justify}
</style>
</head>
<body>

<!-- Cover -->
<section class="page" style="left:20px;top:20px">
  <div class="brand"><span class="brand-square"></span><span class="brand-name">Tavosk Engineering</span></div>
  <div class="cover-photo" role="img" aria-label="Close-up photograph of metal gears and machinery"></div>
  <h1 class="cover-title">Project title</h1>
  <p class="cover-sub">Project subtitle</p>
  <p class="cover-meta">Prepared for client name<br>Report number PLW-001<br>March 2024</p>
</section>

<!-- Contents -->
<section class="page" style="left:238px;top:20px">
  <div class="brand"><span class="brand-square"></span><span class="brand-name">Tavosk Engineering</span></div>
  <div class="band"></div>
  <div class="body">
    <h2 class="h1">Contents</h2>
    <ul class="toc">
      <li>Introduction<span class="dots"></span>3</li>
      <li>Text<span class="dots"></span>3</li>
      <li>Text (Option 2)<span class="dots"></span>4</li>
      <li>Tables<span class="dots"></span>5</li>
      <li>Bar charts<span class="dots"></span>7</li>
      <li>Line chart<span class="dots"></span>8</li>
      <li>Pie charts/combo charts/scatter charts<span class="dots"></span>9</li>
      <li>Disclaimer<span class="dots"></span>10</li>
    </ul>
  </div>
  <div class="footer">2</div>
</section>

<!-- Text -->
<section class="page" style="left:456px;top:20px">
  <div class="brand"><span class="brand-square"></span><span class="brand-name">Tavosk Engineering</span></div>
  <div class="band"></div>
  <div class="body">
    <h2 class="h1">Text</h2>
    <p class="p">This report sets out the findings of the site review and the design basis for the proposed works. Body text is set in a clear sans serif for easy reading on screen and in print.</p>
    <p class="p">Each section opens with a short summary, followed by supporting detail, tables and charts where needed.</p>
    <p class="h3">Sub heading</p>
    <p class="p">Use this style for short notes within a section.</p>
    <p class="h2">Heading 2</p>
    <p class="h2" style="font-size:4.4px">Heading 3</p>
    <p class="h2" style="font-size:4px;color:var(--brand)">Heading 4</p>
    <ul class="list">
      <li>First level bullet point text</li>
      <li>Second bullet point text
        <ul class="list"><li class="sub">Second level bullet text</li><li class="sub">Another second level item</li></ul>
      </li>
      <li>Third bullet point text</li>
    </ul>
  </div>
  <div class="footer">3</div>
</section>

<!-- Text option 2 -->
<section class="page" style="left:20px;top:312px">
  <div class="brand"><span class="brand-square"></span><span class="brand-name">Tavosk Engineering</span></div>
  <div class="band"></div>
  <div class="body">
    <h2 class="h1">Text (Option 2)</h2>
    <ul class="list">
      <li>Numbered or bulleted paragraph text for key findings and recommendations.</li>
      <li>Second paragraph point with a short supporting statement.</li>
      <li>Third paragraph point describing the scope of works.
        <ul class="list"><li class="sub">Sub point with further detail on the item above.</li><li class="sub">Sub point with a second note.</li></ul>
      </li>
      <li>Fourth paragraph point with a closing remark.
        <ul class="list"><li class="sub">Further sub point.</li></ul>
      </li>
    </ul>
  </div>
  <div class="footer">4</div>
</section>

<!-- Tables -->
<section class="page" style="left:238px;top:312px">
  <div class="brand"><span class="brand-square"></span><span class="brand-name">Tavosk Engineering</span></div>
  <div class="band"></div>
  <div class="body">
    <h2 class="h1">Tables</h2>
    <p class="tbl-label">Table style 1</p>
    <table class="tbl-rule">
      <tr><th>Item</th><th class="num">2021</th><th class="num">2022</th><th class="num">2023</th></tr>
      <tr><td>Row one</td><td class="num">120</td><td class="num">140</td><td class="num">165</td></tr>
      <tr><td>Row two</td><td class="num">85</td><td class="num">92</td><td class="num">110</td></tr>
      <tr><td>Row three</td><td class="num">60</td><td class="num">74</td><td class="num">81</td></tr>
      <tr><td>Total</td><td class="num">265</td><td class="num">306</td><td class="num">356</td></tr>
    </table>
    <p class="tbl-label">Table style 2</p>
    <table class="tbl-blue">
      <tr><th>Item</th><th class="num">2021</th><th class="num">2022</th><th class="num">2023</th></tr>
      <tr><td>Row one</td><td class="num">120</td><td class="num">140</td><td class="num">165</td></tr>
      <tr><td>Row two</td><td class="num">85</td><td class="num">92</td><td class="num">110</td></tr>
      <tr><td>Row three</td><td class="num">60</td><td class="num">74</td><td class="num">81</td></tr>
      <tr><td>Row four</td><td class="num">42</td><td class="num">48</td><td class="num">55</td></tr>
    </table>
    <p class="tbl-label">Table style 3</p>
    <table class="tbl-rule">
      <tr><th>Item</th><th class="num">2021</th><th class="num">2022</th><th class="num">2023</th></tr>
      <tr><td>Row one</td><td class="num">120</td><td class="num">140</td><td class="num">165</td></tr>
      <tr><td>Row two</td><td class="num">85</td><td class="num">92</td><td class="num">110</td></tr>
      <tr><td>Row three</td><td class="num">60</td><td class="num">74</td><td class="num">81</td></tr>
    </table>
  </div>
  <div class="footer">5</div>
</section>

<!-- Dark table -->
<section class="page" style="left:456px;top:312px">
  <div class="brand"><span class="brand-square"></span><span class="brand-name">Tavosk Engineering</span></div>
  <div class="band"></div>
  <div class="body">
    <table class="tbl-dark">
      <tr><th>Item</th><th class="num">2021</th><th class="num">2022</th><th class="num">2023</th></tr>
      <tr><td>Row one</td><td class="num">120</td><td class="num">140</td><td class="num">165</td></tr>
      <tr><td>Row two</td><td class="num">85</td><td class="num">92</td><td class="num">110</td></tr>
      <tr><td>Row three</td><td class="num">60</td><td class="num">74</td><td class="num">81</td></tr>
      <tr><td>Row four</td><td class="num">42</td><td class="num">48</td><td class="num">55</td></tr>
    </table>
  </div>
  <div class="footer">6</div>
</section>

<!-- Bar charts -->
<section class="page" style="left:20px;top:604px">
  <div class="brand"><span class="brand-square"></span><span class="brand-name">Tavosk Engineering</span></div>
  <div class="band"></div>
  <div class="body">
    <h2 class="h1">Bar charts</h2>
    <div class="charts">
      <div class="chart"><p class="chart-title">Chart title</p>
        <svg viewBox="0 0 80 52"><line x1="4" y1="44" x2="78" y2="44" stroke="#c9c9c9" stroke-width=".6"/>
          <g fill="#0455a3"><rect x="8" y="24" width="5" height="20"/><rect x="26" y="18" width="5" height="26"/><rect x="44" y="28" width="5" height="16"/><rect x="62" y="12" width="5" height="32"/></g>
          <g fill="#a9c8e8"><rect x="14" y="30" width="5" height="14"/><rect x="32" y="26" width="5" height="18"/><rect x="50" y="22" width="5" height="22"/><rect x="68" y="20" width="5" height="24"/></g>
          <rect x="24" y="48" width="3" height="3" fill="#0455a3"/><rect x="44" y="48" width="3" height="3" fill="#a9c8e8"/></svg></div>
      <div class="chart"><p class="chart-title">Chart title</p>
        <svg viewBox="0 0 80 52"><line x1="4" y1="44" x2="78" y2="44" stroke="#c9c9c9" stroke-width=".6"/>
          <g fill="#0455a3"><rect x="10" y="30" width="8" height="14"/><rect x="28" y="20" width="8" height="24"/><rect x="46" y="14" width="8" height="30"/><rect x="64" y="8" width="8" height="36"/></g>
          <g fill="#3f86c9"><rect x="10" y="22" width="8" height="8"/><rect x="28" y="14" width="8" height="6"/></g></svg></div>
      <div class="chart"><p class="chart-title">Chart title</p>
        <svg viewBox="0 0 80 52"><line x1="10" y1="2" x2="10" y2="46" stroke="#c9c9c9" stroke-width=".6"/>
          <g fill="#0455a3"><rect x="10" y="4" width="50" height="4"/><rect x="10" y="16" width="38" height="4"/><rect x="10" y="28" width="60" height="4"/><rect x="10" y="40" width="28" height="4"/></g>
          <g fill="#a9c8e8"><rect x="10" y="9" width="34" height="4"/><rect x="10" y="21" width="52" height="4"/><rect x="10" y="33" width="24" height="4"/></g></svg></div>
      <div class="chart"><p class="chart-title">Chart title</p>
        <svg viewBox="0 0 80 52"><line x1="10" y1="2" x2="10" y2="46" stroke="#c9c9c9" stroke-width=".6"/>
          <g fill="#0455a3"><rect x="10" y="4" width="40" height="6"/><rect x="10" y="16" width="56" height="6"/><rect x="10" y="28" width="30" height="6"/><rect x="10" y="40" width="48" height="6"/></g>
          <g fill="#a9c8e8"><rect x="50" y="4" width="16" height="6"/><rect x="40" y="28" width="22" height="6"/></g></svg></div>
    </div>
  </div>
  <div class="footer">7</div>
</section>

<!-- Line chart -->
<section class="page" style="left:238px;top:604px">
  <div class="brand"><span class="brand-square"></span><span class="brand-name">Tavosk Engineering</span></div>
  <div class="band"></div>
  <div class="body">
    <h2 class="h1">Line chart</h2>
    <div class="charts">
      <div class="chart"><p class="chart-title">Chart title</p>
        <svg viewBox="0 0 80 52" fill="none" stroke-width="1.2"><line x1="4" y1="44" x2="78" y2="44" stroke="#c9c9c9" stroke-width=".6"/>
          <polyline points="6,30 24,20 42,28 60,14 76,22" stroke="#0455a3"/>
          <polyline points="6,36 24,32 42,20 60,26 76,12" stroke="#a9c8e8"/>
          <polyline points="6,24 24,36 42,34 60,30 76,34" stroke="#5a5a5a"/></svg></div>
      <div class="chart"><p class="chart-title">Chart title</p>
        <svg viewBox="0 0 80 52" fill="none" stroke-width="1.2"><line x1="4" y1="44" x2="78" y2="44" stroke="#c9c9c9" stroke-width=".6"/>
          <polyline points="6,34 24,26 42,22 60,16 76,10" stroke="#0455a3"/>
          <polyline points="6,28 24,30 42,26 60,28 76,24" stroke="#a9c8e8"/></svg></div>
      <div class="chart"><p class="chart-title">Chart title</p>
        <svg viewBox="0 0 80 52"><polygon points="4,44 4,30 22,24 40,30 58,16 78,20 78,44" fill="#0455a3"/>
          <polygon points="4,44 4,38 22,34 40,36 58,28 78,32 78,44" fill="#a9c8e8"/></svg></div>
      <div class="chart"><p class="chart-title">Chart title</p>
        <svg viewBox="0 0 80 52"><polygon points="4,44 4,20 22,26 40,14 58,22 78,10 78,44" fill="#1b1b1b"/>
          <polygon points="4,44 4,32 22,30 40,34 58,26 78,28 78,44" fill="#0455a3"/></svg></div>
    </div>
  </div>
  <div class="footer">8</div>
</section>

<!-- Pie / combo / scatter -->
<section class="page" style="left:456px;top:604px">
  <div class="brand"><span class="brand-square"></span><span class="brand-name">Tavosk Engineering</span></div>
  <div class="band"></div>
  <div class="body">
    <h2 class="h1" style="font-size:9px;line-height:10px">Pie charts/combo charts/scatter charts</h2>
    <div class="charts">
      <div class="chart"><p class="chart-title">Chart title</p>
        <svg viewBox="0 0 80 52"><circle cx="30" cy="26" r="20" fill="#a9c8e8"/>
          <path d="M30 26 L30 6 A20 20 0 0 1 48 35 Z" fill="#0455a3"/>
          <path d="M30 26 L48 35 A20 20 0 0 1 18 42 Z" fill="#3f86c9"/>
          <g fill="#5a5a5a"><rect x="60" y="16" width="3" height="3"/><rect x="60" y="24" width="3" height="3"/><rect x="60" y="32" width="3" height="3"/></g></svg></div>
      <div class="chart"><p class="chart-title">Chart title</p>
        <svg viewBox="0 0 80 52" fill="none" stroke-width="8"><circle cx="40" cy="26" r="18" stroke="#a9c8e8"/>
          <path d="M40 8 A18 18 0 0 1 55 36" stroke="#0455a3"/>
          <path d="M55 36 A18 18 0 0 1 30 41" stroke="#1b1b1b"/></svg></div>
      <div class="chart"><p class="chart-title">Chart title</p>
        <svg viewBox="0 0 80 52"><line x1="4" y1="44" x2="78" y2="44" stroke="#c9c9c9" stroke-width=".6"/>
          <g fill="#0455a3"><rect x="8" y="28" width="7" height="16"/><rect x="26" y="22" width="7" height="22"/><rect x="44" y="16" width="7" height="28"/><rect x="62" y="24" width="7" height="20"/></g>
          <g fill="#a9c8e8"><rect x="16" y="32" width="7" height="12"/><rect x="34" y="30" width="7" height="14"/><rect x="52" y="26" width="7" height="18"/></g>
          <polyline points="12,20 30,12 48,8 66,14" fill="none" stroke="#1b1b1b" stroke-width="1"/></svg></div>
      <div class="chart"><p class="chart-title">Chart title</p>
        <svg viewBox="0 0 80 52"><line x1="6" y1="44" x2="78" y2="44" stroke="#c9c9c9" stroke-width=".6"/><line x1="6" y1="4" x2="6" y2="44" stroke="#c9c9c9" stroke-width=".6"/>
          <g fill="#0455a3"><circle cx="14" cy="36" r="1.6"/><circle cx="24" cy="30" r="1.6"/><circle cx="34" cy="32" r="1.6"/><circle cx="44" cy="22" r="1.6"/><circle cx="54" cy="18" r="1.6"/><circle cx="64" cy="12" r="1.6"/></g>
          <g fill="#a9c8e8"><circle cx="20" cy="20" r="1.6"/><circle cx="40" cy="12" r="1.6"/><circle cx="58" cy="30" r="1.6"/><circle cx="70" cy="24" r="1.6"/></g></svg></div>
    </div>
  </div>
  <div class="footer">9</div>
</section>

<!-- Disclaimer -->
<section class="page disclaimer" style="left:238px;top:896px">
  <div class="brand"><span class="brand-square"></span><span class="brand-name">Tavosk Engineering</span></div>
  <div class="band"></div>
  <div class="body">
    <h2 class="h1">Disclaimer</h2>
    <p class="p">This report has been prepared by Tavosk Engineering for the sole use of the client named on the cover and for the purpose stated within. It should not be relied upon by any other party or for any other purpose without our written consent.</p>
    <p class="p">The findings are based on information available at the time of writing, including site visits, survey data and documents supplied by others. We accept no liability for errors in information provided by third parties.</p>
    <p class="p">Site conditions may change over time. Where conditions differ from those described, the advice in this report should be reviewed before any work proceeds.</p>
    <p class="p">Copyright in this document remains with Tavosk Engineering. No part of it may be copied or shared without permission, except as required for the project it describes.</p>
    <p class="p">All drawings, tables and charts are indicative only and must be read together with the full text of the report and any later revisions issued.</p>
    <p class="p">Questions about the content of this report should be directed to the project lead named in the document control section.</p>
  </div>
  <div class="footer">10</div>
</section>

</body>
</html>
```